T.B.W.L. Business Card Design

we need a business card design for a motor vehicle repair business in Southport Australia, called Trevan's Automotive Repair Services. Our services include panel & paint, resprays and light bodyworks. We have a logo which we would like to use on the business card. We would like to see designs that use the colours blue and grey.

Industry/Entity Type

Automotive

Contact Information for Business Card

Trevan's Automotive Repair Services,
Delwyn Orsk,
7/2-4 Quarrow Street Southport 4215, 0471 862 307, /trevansautomotiverepairservices, trevansautomotiverepairservices@examplemail.test,
services: panel & paint, respray, light bodyworks.
ABN: 47 612 098 254

Requirements
Must have
• Front of card must include attached logo and contact details.
please list services
Your eye should be drawn to the name (Delwyn Orsk) and phone number (0471 862 307).
Font must be legible and contemporary.
back of business card should have the following:
1. title - quote and
2. list the following: for, date, valid till, quote details and
3. a footer "to book you repair, please contact Delwyn Orsk on 0471 862 307".
There needs to be enough space to hand write details.
Should not have
• do not include any graphics/illustrations.

```html
<!DOCTYPE html>
<html lang="en">
<head>
<meta charset="utf-8">
<title>T.B.W.L. Business Card</title>
<link rel="stylesheet" href="https://fonts.googleapis.com/css2?family=Bebas+Neue&family=Open+Sans:wght@400;600;700&display=swap">
<style>
  :root {
    --page-bg: #e2e2e2;
    --card-white: #ffffff;
    --card-grey: #d9d9d9;
    --brand-blue: #2f67b6;
    --ink: #111111;
    --label-grey: #9a9a9a;
    --rule: #1a1a1a;
  }
  * { margin: 0; padding: 0; box-sizing: border-box; }
  html, body { width: 1200px; height: 944px; overflow: hidden; }
  body {
    background: var(--page-bg);
    font-family: "Open Sans", Arial, sans-serif;
    color: var(--ink);
    position: relative;
  }
  .card {
    position: absolute;
    top: 328px;
    width: 400px;
    height: 248px;
  }
  .card-front { left: 165px; background: var(--card-white); }
  .card-back { left: 622px; background: var(--card-grey); }

  /* front */
  .brand-mark {
    position: absolute;
    left: 18px; top: 44px;
    display: flex; align-items: center; gap: 8px;
  }
  .brand-dot {
    width: 14px; height: 14px; border-radius: 50%;
    background: var(--brand-blue);
  }
  .brand-name {
    font-family: "Bebas Neue", sans-serif;
    font-size: 22px;
    line-height: 1;
    color: var(--brand-blue);
    width: 200px;
  }
  .services {
    position: absolute;
    left: 278px; top: 38px;
    list-style: none;
    font-size: 10.5px;
    line-height: 14.5px;
  }
  .divider {
    position: absolute;
    left: 15px; top: 116px;
    width: 371px; height: 2px;
    background: var(--rule);
  }
  .contact {
    position: absolute;
    left: 0; top: 140px; width: 400px;
    text-align: center;
  }
  .contact-business {
    font-family: "Bebas Neue", sans-serif;
    font-size: 20px; line-height: 20px;
    color: var(--brand-blue);
    letter-spacing: 0.3px;
  }
  .contact-address { font-size: 12.5px; line-height: 18px; }
  .contact-phone { font-size: 20px; font-weight: 700; line-height: 30px; margin-top: 2px; }
  .contact-email { font-size: 10px; line-height: 14px; }

  /* back */
  .field {
    position: absolute;
    background: var(--card-white);
  }
  .field-label {
    position: absolute;
    left: 5px; bottom: 2px;
    font-size: 9px; font-weight: 600;
    color: var(--label-grey);
  }
  .field-title { left: 21px; top: 15px; width: 364px; height: 44px; }
  .field-for { left: 21px; top: 63px; width: 364px; height: 40px; }
  .field-date { left: 21px; top: 108px; width: 180px; height: 40px; }
  .field-valid { left: 206px; top: 108px; width: 179px; height: 40px; }
  .field-details { left: 21px; top: 153px; width: 364px; height: 67px; }
  .booking-note {
    position: absolute;
    left: 26px; top: 224px;
    font-size: 11.5px;
    color: var(--label-grey);
    white-space: nowrap;
  }
  .booking-name { color: var(--brand-blue); font-weight: 600; }
  .booking-phone { color: var(--ink); font-weight: 600; }
</style>
</head>
<body>
  <section class="card card-front" aria-label="Business card front">
    <div class="brand-mark">
      <span class="brand-dot"></span>
      <span class="brand-name">Trevan's Automotive Repair Services</span>
    </div>
    <ul class="services">
      <li>Panel &amp; paint</li>
      <li>Respray</li>
      <li>Light bodyworks</li>
      <li>ABN: 47 612 098 254</li>
    </ul>
    <div class="divider"></div>
    <div class="contact">
      <p class="contact-business">Trevan's Automotive Repair Services</p>
      <p class="contact-address">Delwyn Orsk, 7/2-4 Quarrow Street Southport 4215,</p>
      <p class="contact-phone">Phone: 0471 862 307</p>
      <p class="contact-email">trevansautomotiverepairservices@examplemail.test</p>
    </div>
  </section>

  <section class="card card-back" aria-label="Business card back, quote form">
    <div class="field field-title"><span class="field-label">title</span></div>
    <div class="field field-for"><span class="field-label">for</span></div>
    <div class="field field-date"><span class="field-label">date</span></div>
    <div class="field field-valid"><span class="field-label">valid till</span></div>
    <div class="field field-details"><span class="field-label">details</span></div>
    <p class="booking-note">to book you repair, please contact <span class="booking-name">Delwyn Orsk on</span> <span class="booking-phone">0471 862 307</span></p>
  </section>
</body>
</html>
```